BOLD & MINIMALIST DESIGN NEEDED

We want a very bold but minimalistic business card design that is impactful and utilizes both sides of the business card. Our current logo is included for your use.

We want bold fonts and good use of negative space. We don't want the logo to overpower the design.

Target Market(s)

Professionals who are building new commercial buildings.

Industry/Entity Type

Construction

Contact Information for Business Card

Name, Title, email, office phone, cell phone, website

Font styles to use
Serif
Sans Serif

Requirements
Must have
• Bold design!

```html
<!DOCTYPE html>
<html lang="en">
<head>
<meta charset="utf-8">
<title>Ridgeline Build – Business Card</title>
<link href="https://fonts.googleapis.com/css2?family=Poppins:wght@300;400;600;700;800&display=swap" rel="stylesheet">
<style>
  :root {
    --bg: #2b2c2f;
    --card-white: #ffffff;
    --card-dark: #1f2022;
    --pattern-dark: #26272a;
    --ink: #111214;
    --muted: #6b6d70;
    --green: #7cc242;
    --divider: #d9dadb;
  }
  * { box-sizing: border-box; margin: 0; padding: 0; }
  html, body {
    width: 1200px; height: 952px; overflow: hidden;
    background: var(--bg);
    font-family: "Poppins", sans-serif;
  }
  .canvas { position: relative; width: 1200px; height: 952px; }

  .card {
    position: absolute;
    width: 560px; height: 320px;
    border-radius: 3px;
    overflow: hidden;
    box-shadow: 0 18px 40px rgba(0,0,0,.45);
  }

  /* Front */
  .card--front { left: 560px; top: 90px; background: var(--card-white); }
  .corner-band { position: absolute; background: var(--ink); width: 26px; }
  .corner-band--top { left: 0; top: 0; height: 120px; }
  .corner-band--bottom { right: 0; bottom: 0; height: 120px; }

  .brand {
    position: absolute; left: 64px; top: 104px;
    display: flex; align-items: center; gap: 12px;
  }
  .brand__mark { width: 18px; height: 18px; background: var(--green); flex: none; }
  .brand__name {
    font-weight: 800; font-size: 28px; letter-spacing: .5px;
    color: var(--ink); line-height: 1.05;
  }
  .brand__line { display: block; }
  .card--front .divider {
    position: absolute; left: 300px; top: 70px;
    width: 1px; height: 150px; background: var(--divider);
  }
  .person { position: absolute; left: 326px; top: 78px; }
  .person__name { font-size: 19px; color: var(--ink); letter-spacing: .8px; font-weight: 400; line-height: 1.1; }
  .person__name strong { font-weight: 700; }
  .person__title { font-size: 12px; color: var(--muted); margin-top: 4px; }
  .contacts { list-style: none; margin-top: 18px; }
  .contacts li {
    display: flex; align-items: center; gap: 8px;
    font-size: 12px; color: var(--muted); margin-bottom: 7px;
  }
  .contacts svg { width: 12px; height: 12px; fill: var(--green); flex: none; }
  .address {
    position: absolute; left: 64px; bottom: 44px;
    font-size: 11px; color: var(--muted);
  }

  /* Back */
  .card--back { left: 80px; top: 520px; background: var(--card-dark); }
  .back-pattern {
    position: absolute; inset: 0;
    background: linear-gradient(135deg, var(--pattern-dark), var(--card-dark));
  }
  .card--back .brand { left: 190px; top: 150px; }
  .card--back .brand__name { color: #ffffff; }
</style>
</head>
<body>
<main class="canvas">

  <section class="card card--front" aria-label="Business card front">
    <span class="corner-band corner-band--top"></span>
    <span class="corner-band corner-band--bottom"></span>

    <div class="brand">
      <span class="brand__mark"></span>
      <span class="brand__name"><span class="brand__line">RIDGELINE</span><span class="brand__line">BUILD</span></span>
    </div>

    <span class="divider"></span>

    <div class="person">
      <h1 class="person__name">DANIEL M. <strong>CORWIN</strong></h1>
      <p class="person__title">Managing Director</p>
      <ul class="contacts">
        <li>
          <svg viewBox="0 0 24 24" aria-hidden="true"><path d="M6.6 10.8a15.1 15.1 0 0 0 6.6 6.6l2.2-2.2a1 1 0 0 1 1-.25 11.4 11.4 0 0 0 3.6.57 1 1 0 0 1 1 1V20a1 1 0 0 1-1 1A17 17 0 0 1 3 4a1 1 0 0 1 1-1h3.5a1 1 0 0 1 1 1c0 1.25.2 2.45.57 3.57a1 1 0 0 1-.25 1z"/></svg>
          +00 987 654 32
        </li>
        <li>
          <svg viewBox="0 0 24 24" aria-hidden="true"><path d="M2 5h20v14H2z M2 5l10 8 10-8" /></svg>
          hello@ridgelinebuild.com
        </li>
        <li>
          <svg viewBox="0 0 24 24" aria-hidden="true"><circle cx="12" cy="12" r="10"/></svg>
          www.ridgelinebuild.com
        </li>
      </ul>
    </div>

    <p class="address">1520 Harbor Crest Avenue Portland, OR 97205</p>
  </section>

  <section class="card card--back" aria-label="Business card back">
    <div class="back-pattern" role="img" aria-label="Faint repeating brand pattern on dark background"></div>
    <div class="brand">
      <span class="brand__mark"></span>
      <span class="brand__name"><span class="brand__line">RIDGELINE</span><span class="brand__line">BUILD</span></span>
    </div>
  </section>

</main>
</body>
</html>
```